Packaging design for handmade soap

We are looking for a packaging design for a brand new product line: handmade soaps, called BRIVO

We are looking for a design of an outer box together with the logo. We need the design for a 90x65x30mm box (see attached). We trying to get a high-end product preferable with vintage elements (but we don't want a shiny box, it will be finished with matte lacque, however logo or other certain elements could be shiny).

The design should reflect the fact that we have a handmade, all natural soap.

I uploaded a couple of packaging examples I like.

UPDATE 1: It also should have a title, which describes the product more accurate, like "Natural Soap with Seabuckthorn and Olive oil"

UPDATE 2: I would remove the expression "high-end" from the description if high end would mean a lot of flowers in the background. I would like if you would insist about the ideea of "natural" in your works

UPDATE 3: Prefered colors green and brown (which brings the ideea of nature, natural)

Target Market(s)

Women 20-45 years with above average income

Industry/Entity Type

Cosmetics

Font styles to use
Serif

Colors
9bcb3c
acd036
cadf82
f78f20
ffc214
f37122
fbed22
fece3e
faa54b

Requirements
Must have
• A literal representation of the brand BRIVO (we don't have a logo for it)

```html
<!DOCTYPE html>
<html lang="en">
<head>
<meta charset="utf-8">
<title>BRIVO – Natural Soap Box Front</title>
<link rel="stylesheet" href="https://fonts.googleapis.com/css2?family=Lora:wght@600;700&family=Playfair+Display:wght@600&display=swap">
<style>
  :root {
    --page-bg: #f3f3f1;
    --kraft: #b8a789;
    --kraft-dark: #a6946f;
    --band-white: #ffffff;
    --leaf-light: #cadf82;
    --leaf-mid: #acd036;
    --frame-green: #9bcb3c;
    --text-green: #5b8a18;
    --text-brown: #6b5536;
  }
  * { margin: 0; padding: 0; box-sizing: border-box; }
  html, body {
    width: 1200px;
    height: 1000px;
    overflow: hidden;
    background: var(--page-bg);
  }
  .canvas {
    position: relative;
    width: 1200px;
    height: 1000px;
  }
  .box-front {
    position: absolute;
    left: 320px;
    top: 140px;
    width: 560px;
    height: 720px;
    background: linear-gradient(180deg, var(--kraft) 0%, var(--kraft-dark) 100%);
  }
  .label-band {
    position: absolute;
    left: 0;
    top: 144px;
    width: 560px;
    height: 420px;
    background: var(--band-white);
  }
  .label-band svg {
    position: absolute;
    inset: 0;
    width: 560px;
    height: 420px;
  }
  .label-text {
    position: absolute;
    inset: 0;
    display: flex;
    flex-direction: column;
    align-items: center;
    justify-content: center;
    text-align: center;
  }
  .brand-name {
    font-family: "Playfair Display", serif;
    font-size: 84px;
    font-weight: 600;
    letter-spacing: 3px;
    line-height: 1;
    color: var(--text-green);
    margin-bottom: 18px;
  }
  .product-title {
    font-family: "Lora", serif;
    font-size: 19px;
    font-weight: 700;
    line-height: 1.35;
    color: var(--text-brown);
  }
</style>
</head>
<body>
  <main class="canvas">
    <section class="box-front">
      <div class="label-band">
        <svg viewBox="0 0 560 420" xmlns="http://www.w3.org/2000/svg">
          <defs>
            <linearGradient id="patternTone" x1="0" y1="0" x2="1" y2="1">
              <stop offset="0" stop-color="var(--leaf-light)"/>
              <stop offset="1" stop-color="var(--leaf-mid)"/>
            </linearGradient>
          </defs>
          <rect class="damask-pattern" x="0" y="0" width="560" height="420" fill="url(#patternTone)" role="img" aria-label="Vintage damask pattern on the label band"/>
          <g class="cartouche" transform="translate(0 -0) scale(1 1.4)">
            <path class="cartouche-fill"
              d="M100 30 L225 30 Q230 30 232 21 Q240 8 280 8 Q320 8 328 21 Q330 30 335 30 L460 30 Q460 62 492 62 L492 238 Q460 238 460 270 L335 270 Q330 270 328 279 Q320 292 280 292 Q240 292 232 279 Q230 270 225 270 L100 270 Q100 238 68 238 L68 62 Q100 62 100 30 Z"
              fill="var(--band-white)" stroke="var(--frame-green)" stroke-width="7" vector-effect="non-scaling-stroke"/>
            <path class="cartouche-inner-line"
              d="M100 30 L225 30 Q230 30 232 21 Q240 8 280 8 Q320 8 328 21 Q330 30 335 30 L460 30 Q460 62 492 62 L492 238 Q460 238 460 270 L335 270 Q330 270 328 279 Q320 292 280 292 Q240 292 232 279 Q230 270 225 270 L100 270 Q100 238 68 238 L68 62 Q100 62 100 30 Z"
              transform="translate(280 150) scale(0.9) translate(-280 -150)"
              fill="none" stroke="var(--frame-green)" stroke-width="2.5" vector-effect="non-scaling-stroke"/>
          </g>
        </svg>
        <div class="label-text">
          <h1 class="brand-name">BRIVO</h1>
          <p class="product-title">Natural Soap with<br>Seabuckthorn and Olive oil</p>
        </div>
      </div>
    </section>
  </main>
</body>
</html>
```